Bramwell Hockey Academy

We are are Ice Hockey Development Company that provided on-ice Hockey development services. We need a Landing Page with tabs to direct to individual program pages.
Landing Page
About Page
Winter Program Page
Spring Program Page
Summer Program Page
Team Page
Tournament Page

```html
<!DOCTYPE html>
<html lang="en">
<head>
<meta charset="utf-8">
<title>Bramwell Hockey Academy</title>
<link rel="stylesheet" href="https://fonts.googleapis.com/css2?family=Bebas+Neue&family=Oswald:wght@500&family=Manrope:wght@400;500;600;700&display=swap">
<style>
:root{
  --green:#1f8a24;
  --green-dark:#146a18;
  --ink:#111111;
  --text:#2d2d2d;
  --muted:#9a9a9a;
  --pale:#e9eef4;
  --white:#ffffff;
  --black:#000000;
}
*{margin:0;padding:0;box-sizing:border-box}
html,body{width:1200px;height:3607px;overflow:hidden;background:var(--white)}
body{position:relative;font-family:"Manrope",sans-serif;color:var(--text)}
.abs{position:absolute}
.display{font-family:"Bebas Neue",sans-serif;color:var(--ink);font-weight:400;line-height:1}
.eyebrow{font-size:11px;font-weight:700;color:var(--green);text-transform:uppercase;letter-spacing:.2px}
.pill{display:flex;align-items:center;justify-content:center;background:var(--green);color:var(--white);border-radius:30px;font-weight:700;font-size:14px}
.photo{position:absolute}

/* header */
.site-header{left:0;top:0;width:1200px;height:80px;background:var(--white)}
.brand{left:164px;top:24px;font-family:"Bebas Neue",sans-serif;font-size:30px;color:var(--ink);display:flex;align-items:center;gap:8px}
.brand-dot{width:14px;height:14px;border-radius:50%;background:var(--green)}
.nav{left:427px;top:33px;font-size:14px;font-weight:600;color:var(--ink)}
.nav a{position:absolute;white-space:nowrap;color:inherit;text-decoration:none}
.join-top{left:930px;top:21px;width:128px;height:35px;font-size:15px}

/* hero */
.hero{left:0;top:80px;width:1200px;height:655px}
.hero-photo{left:0;top:0;width:1200px;height:655px;background:linear-gradient(90deg,#f4f5f6 0%,#eef0f2 45%,#c9d2dc 62%,#6d85a6 72%,#e5e8ec 88%,#f3f4f5 100%)}
.hero-title{left:144px;top:213px;font-size:60px}
.hero-title span{display:block;height:58px}
.hero-copy{left:147px;top:337px;width:520px;font-size:12.5px;font-weight:600;line-height:26px;color:var(--ink)}
.hero-btn{left:147px;top:411px;width:176px;height:43px}
.slider-ctrl{left:70px;top:245px;width:20px;height:160px}
.scroll-btn{left:575px;top:624px;width:54px;height:54px;border-radius:50%;background:var(--green)}

/* programs */
.programs-eyebrow{left:0;top:781px;width:1200px;text-align:center}
.programs-title{left:0;top:812px;width:1200px;text-align:center;font-size:36px;line-height:43px}
.program-card{top:928px;width:290px;height:360px}
.program-card .photo{inset:0}
.program-label{position:absolute;left:11px;right:11px;top:297px;height:53px;background:var(--white);display:flex;align-items:center;justify-content:center;font-family:"Bebas Neue",sans-serif;font-size:20px;color:var(--ink)}
.program-label.active{color:var(--green)}

/* about */
.about{left:0;top:1365px;width:1200px;height:518px;background:var(--pale)}
.about-frame{left:158px;top:77px;width:345px;height:382px;border:1px solid #9aa7a0}
.about-photo{left:144px;top:63px;width:345px;height:382px;background:linear-gradient(160deg,#3a4c66 0%,#5a6f8c 35%,#c23a2e 55%,#d9dee4 80%,#eef1f4 100%)}
.about-eyebrow{left:616px;top:53px}
.about-title{left:616px;top:80px;font-size:40px;line-height:54px}
.about-copy{left:616px;top:198px;width:444px;font-size:12.5px;line-height:21px;color:var(--text)}
.about-copy p+p{margin-top:21px}

/* tournament */
.tour-eyebrow{left:0;top:1919px;width:1200px;text-align:center}
.tour-title{left:0;top:1947px;width:1200px;text-align:center;font-size:40px}
.tour-card{top:2026px;width:236px;height:262px;background:#f6f6f6;border:2px solid #c9c9c9;padding:26px 26px 0}
.tour-card.featured{background:var(--green);border-color:var(--green);color:var(--white)}
.tour-year{font-family:"Bebas Neue",sans-serif;font-size:24px;color:var(--green);line-height:1}
.tour-name{font-family:"Bebas Neue",sans-serif;font-size:18px;color:var(--ink);margin-top:8px;line-height:1}
.featured .tour-year,.featured .tour-name{color:var(--white)}
.tour-date{display:inline-block;margin-top:14px;padding:3px 12px;border-radius:20px;background:var(--green);color:var(--white);font-size:9px;font-weight:700}
.featured .tour-date{background:var(--green-dark)}
.tour-place{margin-top:14px;font-size:9.5px;font-weight:700;color:var(--ink)}
.featured .tour-place{color:var(--white)}
.tour-text{margin-top:18px;font-size:12px;line-height:21px}
.tour-join{top:2271px;width:130px;height:33px;font-size:14px;font-weight:600}
.featured-join{background:var(--green-dark)}
.arrow-btn{top:2138px;width:36px;height:36px;border-radius:50%;background:var(--green)}

/* team */
.team{left:0;top:2392px;width:1200px;height:590px;background:var(--pale)}
.team-eyebrow{left:0;top:61px;width:1200px;text-align:center}
.team-title{left:0;top:88px;width:1200px;text-align:center;font-size:40px}
.member{top:166px;width:214px;text-align:center}
.member .photo{position:relative;width:214px;height:260px}
.member-name{margin-top:20px;font-family:"Bebas Neue",sans-serif;font-size:16px;color:var(--ink)}
.member-role{margin-top:6px;font-size:12.5px;color:var(--muted)}
.member.highlight{background:var(--white);height:365px;border-bottom:7px solid var(--green)}
.read-bio{margin-top:12px;font-size:8px;font-weight:700;color:var(--ink);display:flex;justify-content:center;align-items:center;gap:8px}

/* newsletter */
.newsletter{left:0;top:2982px;width:1200px;height:291px}
.newsletter-photo{left:0;top:0;width:1200px;height:291px;background:linear-gradient(90deg,#eceff2 0%,#e7eaee 55%,#dfe3e8 70%,#e8ebee 100%)}
.news-title{left:143px;top:88px;font-family:"Oswald",sans-serif;font-weight:500;font-size:29px;color:var(--ink)}
.news-sub{left:143px;top:139px;font-size:10px;color:var(--ink)}
.news-form{left:144px;top:179px;width:371px;height:48px;border:2px solid #8d9096;background:var(--white)}
.news-field{left:46px;top:14px;font-size:12px;color:var(--muted)}
.news-btn{left:243px;top:4px;width:120px;height:36px;background:var(--green);color:var(--white);font-size:9px;font-weight:700;display:flex;align-items:center;justify-content:center}

/* footer */
.site-footer{left:0;top:3273px;width:1200px;height:334px;background:var(--black);color:var(--white)}
.footer-rule{top:0;width:1px;height:334px;background:#3a3a3a}
.footer-title{font-family:"Bebas Neue",sans-serif;font-size:18px;color:var(--green)}
.contact-item{left:172px;font-size:11.5px;line-height:24px;display:flex;align-items:flex-start;gap:21px}
.contact-icon{flex:0 0 20px;display:flex;justify-content:center;align-items:center;height:24px}
.footer-brand{left:441px;width:405px;top:86px;text-align:center;font-family:"Bebas Neue",sans-serif;font-size:34px;color:var(--white)}
.socials{left:592px;top:180px;display:flex;gap:12px}
.socials span{width:22px;height:22px;border-radius:50%;background:var(--green)}
.credits{left:441px;width:405px;top:237px;text-align:center;font-size:9px;line-height:17px;color:#cfcfcf}
.menu{left:876px;top:122px;font-size:11px;line-height:28px;list-style:none}
</style>
</head>
<body>

<header class="site-header abs">
  <div class="brand abs"><span class="brand-dot"></span>Bramwell Hockey</div>
  <nav class="nav abs">
    <a style="left:0">About us</a>
    <a style="left:85px">Our Programs</a>
    <a style="left:207px">Tournament</a>
    <a style="left:322px">Team</a>
    <a style="left:381px">Contact us</a>
  </nav>
  <div class="pill join-top abs">Join us</div>
</header>

<section class="hero abs">
  <div class="photo hero-photo" role="img" aria-label="Adult teaching a smiling child to skate with a hockey stick on an outdoor rink beside a net in the snow"></div>
  <svg class="slider-ctrl abs" viewBox="0 0 20 160" width="20" height="160">
    <circle cx="8" cy="8" r="7" fill="none" stroke="#1f8a24" stroke-width="1.5"/>
    <circle cx="8" cy="8" r="3.5" fill="#1f8a24"/>
    <circle cx="8" cy="36" r="3" fill="#111"/>
    <circle cx="8" cy="57" r="3" fill="#111"/>
    <line x1="8" y1="72" x2="8" y2="142" stroke="#555" stroke-width="1"/>
  </svg>
  <div class="abs" style="left:70px;top:398px;font-size:11px;font-weight:600;color:#111">1/3</div>
  <h1 class="display hero-title abs"><span>Bramwell</span><span>Ice Hockey Development</span></h1>
  <p class="hero-copy abs">Think you feel too tired to work out? Think again. Your fatigue may be mental rather than physical. Here’s how to tell and how to coerce yourself into a training</p>
  <div class="pill hero-btn abs">Our Programs</div>
  <div class="scroll-btn abs">
    <svg viewBox="0 0 54 54" width="54" height="54"><rect x="22" y="15" width="10" height="16" rx="5" fill="none" stroke="#fff" stroke-width="1.5"/><line x1="27" y1="19" x2="27" y2="23" stroke="#fff" stroke-width="1.5"/><path d="M24 35l3 3 3-3" fill="none" stroke="#fff" stroke-width="1.5"/></svg>
  </div>
</section>

<section class="programs">
  <div class="eyebrow programs-eyebrow abs">Our Special Programs</div>
  <h2 class="display programs-title abs">We Providing The<br>Ultimate Ice Hockey Experience ...</h2>
  <article class="program-card abs" style="left:144px">
    <div class="photo" role="img" aria-label="Children skating and stickhandling on a frozen outdoor pond" style="background:linear-gradient(180deg,#b9c3cf 0%,#8e9aab 50%,#c8d0da 100%)"></div>
    <div class="program-label">Winter Program</div>
  </article>
  <article class="program-card abs" style="left:458px">
    <div class="photo" role="img" aria-label="Child in a blue jacket and knit hat holding a hockey stick on snowy ice" style="background:linear-gradient(180deg,#c7b9ad 0%,#d9dde2 40%,#2f9fd3 60%,#eef2f5 100%)"></div>
    <div class="program-label active">Spring Program</div>
  </article>
  <article class="program-card abs" style="left:769px">
    <div class="photo" role="img" aria-label="Young players in red jerseys on an outdoor rink with autumn trees behind" style="background:linear-gradient(180deg,#d9a066 0%,#c86b3a 35%,#d63a34 60%,#e8ecf0 100%)"></div>
    <div class="program-label">Summer Program</div>
  </article>
</section>

<section class="about abs">
  <div class="about-frame abs"></div>
  <div class="photo about-photo" role="img" aria-label="Young player in a red uniform and helmet skating with the puck in an indoor arena"></div>
  <div class="eyebrow about-eyebrow abs">About us</div>
  <h2 class="display about-title abs">Welcome To<br>Bramwell Ice Hockey Development</h2>
  <div class="about-copy abs">
    <p>Li Europan lingues es membres del sam familie. Lor separat existentie es un myth. Por scientie, musica, sport etc, litot Europa usa li sam vocabular. Li lingues differe solmen in li grammatica, li pronunciation e li plu commun vocabules. Omnicos directe al desirabilite de un nov lingua franca: On refusa continuar payar custosi traductores.</p>
    <p>At solmen va esser necessi far uniform grammatica, pronunciation e plu sommun paroles. Ma quande lingues coalesce, li grammatica del resultant lingue es plu simplic e regulari quam ti del coalescent lingues. Li nov lingua franca va esser plu simplic e regulari quam li existent Europan lingues.</p>
  </div>
</section>

<section class="tournament">
  <div class="eyebrow tour-eyebrow abs">Tournament</div>
  <h2 class="display tour-title abs">Bramwell Hockey Tournament</h2>
  <div class="arrow-btn abs" style="left:145px"><svg viewBox="0 0 36 36" width="36" height="36"><path d="M20 12l-6 6 6 6" fill="none" stroke="#fff" stroke-width="1.6"/></svg></div>
  <div class="arrow-btn abs" style="left:1021px"><svg viewBox="0 0 36 36" width="36" height="36"><path d="M16 12l6 6-6 6" fill="none" stroke="#fff" stroke-width="1.6"/></svg></div>

  <article class="tour-card abs" style="left:221px">
    <div class="tour-year">2023 Bramwell</div>
    <div class="tour-name">Ice Hockey Tournament</div>
    <div class="tour-date">23rd March</div>
    <div class="tour-place">FINLAND &amp; LATVIA, Tampere, Riga</div>
    <p class="tour-text">Lorem ipsum dolor sit amet, consectetuer adipiscing elit. Aenean commodo</p>
  </article>
  <article class="tour-card featured abs" style="left:484px">
    <div class="tour-year">2023 Bramwell</div>
    <div class="tour-name">Ice Hockey Tournament</div>
    <div class="tour-date">23rd March</div>
    <div class="tour-place">FINLAND &amp; LATVIA, Tampere, Riga</div>
    <p class="tour-text">Lorem ipsum dolor sit amet, consectetuer adipiscing elit. Aenean commodo</p>
  </article>
  <article class="tour-card abs" style="left:745px">
    <div class="tour-year">2023 Bramwell</div>
    <div class="tour-name">Ice Hockey Tournament</div>
    <div class="tour-date">23rd March</div>
    <div class="tour-place">FINLAND &amp; LATVIA, Tampere, Riga</div>
    <p class="tour-text">Lorem ipsum dolor sit amet, consectetuer adipiscing elit. Aenean commodo</p>
  </article>
  <div class="pill tour-join abs" style="left:244px">Join us</div>
  <div class="pill tour-join featured-join abs" style="left:506px">Join us</div>
  <div class="pill tour-join abs" style="left:766px">Join us</div>
</section>

<section class="team abs">
  <div class="eyebrow team-eyebrow abs">Our Team</div>
  <h2 class="display team-title abs">Meet Our Expert Instructors</h2>
  <article class="member abs" style="left:144px">
    <div class="photo" role="img" aria-label="Instructor in a red and black jersey holding a stick under arena lights" style="background:linear-gradient(180deg,#2e6a8e 0%,#1d2a36 45%,#8a1f22 75%,#2a2a2a 100%)"></div>
    <div class="member-name">Owen Marlow</div>
    <div class="member-role">President &amp; CEO</div>
  </article>
  <article class="member abs" style="left:378px">
    <div class="photo" role="img" aria-label="Goaltender in a green jersey and white helmet against a dark wall" style="background:linear-gradient(180deg,#3a3d3f 0%,#262829 45%,#1f7a3a 80%,#1c1c1c 100%)"></div>
    <div class="member-name">Dane Ridley</div>
    <div class="member-role">General Manager &amp; part owner</div>
  </article>
  <article class="member highlight abs" style="left:612px">
    <div class="photo" role="img" aria-label="Bearded instructor in a blue jersey and helmet holding a stick" style="background:linear-gradient(180deg,#4a4e54 0%,#2d3136 40%,#1f4f9a 75%,#26282b 100%)"></div>
    <div class="member-name">Tomas Ekvall</div>
    <div class="member-role">Sales &amp; All Programming</div>
    <div class="read-bio">READ BIO <svg width="12" height="8" viewBox="0 0 12 8"><path d="M0 4h10M7 1l3 3-3 3" fill="none" stroke="#111" stroke-width="1"/></svg></div>
  </article>
  <article class="member abs" style="left:844px">
    <div class="photo" role="img" aria-label="Instructor in a red and black jersey shouting on the ice under arena lights" style="background:linear-gradient(180deg,#3a7aa0 0%,#1d2a36 45%,#8a1f22 75%,#2a2a2a 100%)"></div>
    <div class="member-name">Reid Carden</div>
    <div class="member-role">Plant Manager</div>
  </article>
</section>

<section class="newsletter abs">
  <div class="photo newsletter-photo" role="img" aria-label="Overhead view of two young players in orange and black uniforms chasing the puck on white ice"></div>
  <div class="abs" role="img" aria-label="Two young players seen from above" style="left:680px;top:40px;width:380px;height:230px;background:radial-gradient(ellipse at 30% 40%,#c9683a 0%,rgba(201,104,58,0) 45%),radial-gradient(ellipse at 75% 55%,#2b2b2b 0%,rgba(43,43,43,0) 42%)"></div>
  <h2 class="news-title abs">Subscribe To Our Newsletter</h2>
  <p class="news-sub abs">Subscribe to our mailing list for news, updates and exclusive offers!</p>
  <form class="news-form abs">
    <svg class="abs" style="left:18px;top:15px" width="18" height="14" viewBox="0 0 18 14"><rect x="1" y="1" width="16" height="12" rx="1.5" fill="none" stroke="#555" stroke-width="1.2"/><path d="M1.5 2l7.5 6 7.5-6" fill="none" stroke="#555" stroke-width="1.2"/></svg>
    <span class="news-field abs">Enter Your Email Address</span>
    <span class="news-btn abs">SUBSCRIBE</span>
  </form>
</section>

<footer class="site-footer abs">
  <div class="footer-rule abs" style="left:144px;height:30px;top:90px"></div>
  <div class="footer-rule abs" style="left:441px"></div>
  <div class="footer-rule abs" style="left:846px"></div>

  <h3 class="footer-title abs" style="left:174px;top:75px">Contact Details</h3>
  <div class="contact-item abs" style="top:120px">
    <span class="contact-icon"><svg width="16" height="20" viewBox="0 0 16 20"><path d="M8 19s-6-7-6-11a6 6 0 0112 0c0 4-6 11-6 11z" fill="none" stroke="#fff" stroke-width="1.2"/><circle cx="8" cy="8" r="2.2" fill="none" stroke="#fff" stroke-width="1.2"/></svg></span>
    <span>418 Larchmont Road<br>Halden Falls, 40211</span>
  </div>
  <div class="contact-item abs" style="top:184px">
    <span class="contact-icon"><svg width="16" height="16" viewBox="0 0 16 16"><path d="M3 1.5l3 3-1.5 2a9 9 0 005 5l2-1.5 3 3-2 2C7 14 2 9 1 3.5z" fill="none" stroke="#fff" stroke-width="1.2"/></svg></span>
    <span>555-014-2290</span>
  </div>
  <div class="contact-item abs" style="top:226px">
    <span class="contact-icon"><svg width="18" height="16" viewBox="0 0 18 16"><rect x="4" y="1" width="10" height="4" fill="none" stroke="#fff" stroke-width="1.2"/><rect x="1" y="5" width="16" height="7" rx="1" fill="none" stroke="#fff" stroke-width="1.2"/><rect x="4" y="10" width="10" height="5" fill="none" stroke="#fff" stroke-width="1.2"/></svg></span>
    <span>555-014-2291</span>
  </div>
  <div class="contact-item abs" style="top:268px">
    <span class="contact-icon"><svg width="16" height="12" viewBox="0 0 16 12"><rect x="1" y="1" width="14" height="10" rx="1" fill="none" stroke="#fff" stroke-width="1.2"/><path d="M1.5 2l6.5 5 6.5-5" fill="none" stroke="#fff" stroke-width="1.2"/></svg></span>
    <span>hello@bramwellhockey.test</span>
  </div>

  <div class="footer-brand abs">Bramwell Hockey</div>
  <div class="socials abs"><span></span><span></span><span></span></div>
  <p class="credits abs">©2023 Bramwell Hockey Academy. All Rights Reserved. TERMS &amp;<br>CONDITIONS</p>

  <h3 class="footer-title abs" style="left:876px;top:75px">Our Top Menu</h3>
  <ul class="menu abs">
    <li>Home</li><li>About us</li><li>Our Programs</li><li>Tournament</li><li>Team</li><li>Contact us</li>
  </ul>
</footer>

</body>
</html>
```